Looking for a hot sauce label designed
Name: Copper Lantern Hot sauce
Graphic: dragon in pictures supplied and the flame bigger going out in front of the dragon or happy for you to design a dragon in a similar style
Text font: using the text supplied for the name of the product only
Colour: Black graphic and text on light brown paper
Style: sketch dragon and text - simple minimalistic design
Label size: 7cm height x 17cm width

Target Market(s)

To sell in bars and supermarkets

Font styles to use
Script

Colors

Designer to choose only greyscale colors for use in the design.

Requirements
Must have
• Name of product: Copper Lantern Hot Sauce
Batch No:
Business name and address
Best before date:
Nutrition Information Panel
Ingredients
Shake well before use
Keep refrigerated after opening
Australian made using 100% local ingredients
175ml
Room for a barcode
Nice to have
• Any changes you think will improve label design

```html
<!DOCTYPE html>
<html lang="en">
<head>
<meta charset="utf-8">
<title>Copper Lantern Hot Sauce – Label</title>
<link href="https://fonts.googleapis.com/css2?family=Indie+Flower&family=Source+Sans+3:wght@400;600;700&display=swap" rel="stylesheet">
<style>
  :root {
    --page: #000000;
    --label-edge: #b7c1d3;
    --label-mid: #e4e8f0;
    --label-white: #ffffff;
    --panel-border: #b9c2d3;
    --ink: #231f20;
    --name-dark: #231f20;
    --name-mid: #4a4a4a;
    --name-soft: #6a6a6a;
    --name-deep: #333333;
    --art-light: #f4f5f7;
    --art-mid: #d9dbde;
    --art-dark: #b9bcc0;
  }
  * { box-sizing: border-box; margin: 0; padding: 0; }
  html, body {
    width: 1200px; height: 900px; overflow: hidden;
    background: var(--page);
    font-family: "Source Sans 3", "Myriad Pro", Arial, sans-serif;
    color: var(--ink);
  }
  .label {
    position: absolute; left: 21px; top: 138px;
    width: 1164px; height: 620px;
    background: linear-gradient(90deg,
      var(--label-edge) 0%, var(--label-mid) 22%, var(--label-white) 40%,
      var(--label-white) 88%, var(--label-mid) 94%, var(--label-edge) 100%);
  }
  .panel {
    position: absolute; background: var(--label-white);
    border: 2px solid var(--panel-border);
  }
  .nutrition { left: 31px; top: 119px; width: 267px; height: 277px; padding: 14px 0 0 24px; font-size: 13.6px; line-height: 18.3px; }
  .nutrition h2 { font-size: 17px; font-weight: 600; margin-bottom: 6px; }
  .nutrition table { border-collapse: collapse; }
  .nutrition td { padding: 0; vertical-align: top; white-space: nowrap; }
  .nutrition .meta td:first-child { width: 168px; }
  .nutrition .values { margin-top: 13px; }
  .nutrition .values td:first-child { width: 120px; }
  .nutrition .values td:nth-child(2) { width: 48px; }
  .caution { left: 31px; top: 409px; width: 267px; height: 161px; padding: 12px 0 0 24px; }
  .caution h2 { font-size: 17px; font-weight: 600; line-height: 20px; }
  .caution ul { list-style: none; font-size: 14.3px; font-weight: 600; line-height: 18.5px; }
  .caution li::before { content: "-"; display: inline-block; width: 14px; }
  .ingredients { margin-top: 11px; font-size: 12.5px; line-height: 15px; padding-right: 44px; }
  .ingredients strong { font-size: 14px; font-weight: 700; }
  .product-name {
    position: absolute; left: 488px; top: 108px; width: 440px;
    font-family: "Indie Flower", "Comic Sans MS", cursive; font-weight: 400;
  }
  .product-name .line1 { display: block; font-size: 60px; line-height: 72px; letter-spacing: 2px; white-space: nowrap; }
  .product-name .copper { color: var(--name-dark); }
  .product-name .lantern { color: var(--name-mid); }
  .product-name .line2 { display: block; font-size: 56px; line-height: 60px; margin-left: 110px; white-space: nowrap; }
  .product-name .hot { color: var(--name-soft); margin-right: 30px; }
  .product-name .sauce { color: var(--name-deep); font-size: 44px; }
  .usage {
    position: absolute; left: 425px; top: 282px; width: 190px;
    font-size: 12.5px; line-height: 16px;
  }
  .usage .storage { font-weight: 600; }
  .usage .best-before { margin-top: 6px; }
  .usage .fill { display: inline-block; width: 84px; border-bottom: 1px solid var(--ink); margin-left: 4px; }
  .usage .maker { margin-top: 6px; }
  .barcode-space {
    position: absolute; left: 425px; top: 400px; width: 170px; height: 100px;
    background: var(--label-white); border: 1.5px dashed var(--panel-border);
  }
  .volume { position: absolute; left: 425px; top: 528px; font-size: 23px; font-weight: 600; }
  .dragon-art {
    position: absolute; left: 627px; top: 309px; width: 383px; height: 255px;
    background: radial-gradient(ellipse at 45% 55%, var(--art-light) 0%, var(--art-mid) 55%, var(--art-dark) 100%);
    border-radius: 40% 30% 20% 35%;
  }
  .origin-note { position: absolute; left: 1092px; top: 119px; width: 36px; height: 190px; }
  .origin-note p {
    position: absolute; left: 50%; top: 50%; width: 190px;
    transform: translate(-50%, -50%) rotate(-90deg);
    font-size: 14.5px; line-height: 20px; white-space: nowrap;
  }
  .batch {
    position: absolute; left: 1089px; top: 402px; width: 42px; height: 168px;
    background: var(--label-white); border: 2px solid var(--panel-border);
  }
  .batch p {
    position: absolute; left: 50%; top: 50%; width: 150px;
    transform: translate(-50%, -50%) rotate(-90deg);
    font-size: 14.5px; white-space: nowrap;
  }
  .batch .blank { display: inline-block; width: 76px; border-bottom: 1.5px solid var(--ink); margin-left: 4px; }
</style>
</head>
<body>
  <main class="label">
    <section class="panel nutrition">
      <h2>NUTRITION INFOMATION</h2>
      <table class="meta">
        <tr><td>Serving per package:</td><td>17.00</td></tr>
        <tr><td>Serving size</td><td>170.00m</td></tr>
      </table>
      <table class="values">
        <tr><td></td><td>Ave.per<br>&nbsp;&nbsp;serve</td><td>&nbsp;Ave.per<br>100m</td></tr>
        <tr><td>Energy</td><td>&nbsp;&nbsp;275g</td><td>151 KJ</td></tr>
        <tr><td>Protein</td><td>&nbsp;&nbsp;1.5g</td><td>0.9g</td></tr>
        <tr><td>Fat, Total</td><td>&nbsp;&nbsp;3.2g</td><td>1.9g</td></tr>
        <tr><td>&nbsp;-saturated</td><td>&nbsp;&nbsp;0.5g</td><td>0.3g</td></tr>
        <tr><td>Carbohydrate</td><td>&nbsp;&nbsp;4.3g</td><td>2.5g</td></tr>
        <tr><td>&nbsp;-sugars</td><td>&nbsp;&nbsp;3.7g</td><td>2.2g</td></tr>
        <tr><td>Sodium</td><td>&nbsp;&nbsp;262g</td><td>154mg</td></tr>
      </table>
    </section>

    <section class="panel caution">
      <h2>CAUTION:</h2>
      <ul>
        <li>Keep out of reach of children</li>
        <li>Keep away and out of eyes</li>
      </ul>
      <p class="ingredients"><strong>INGREDIENTS:</strong> Carrots, Onion, Habanero, water, lime juice, garlic, white, vinegar, vegetable oil, ginger, salt, pepper</p>
    </section>

    <h1 class="product-name">
      <span class="line1"><span class="copper">Copper</span> <span class="lantern">Lantern</span></span>
      <span class="line2"><span class="hot">Hot</span><span class="sauce">sauce</span></span>
    </h1>

    <section class="usage">
      <p class="storage">Shake well before use</p>
      <p class="storage">Keep refrigerated after opening</p>
      <p class="best-before">Best before:<span class="fill"></span></p>
      <p class="maker">Copper Lantern Sauce Co.<br>14 Ember Lane, Kettleridge QLD 4999</p>
    </section>

    <div class="barcode-space" role="img" aria-label="Space reserved for barcode"></div>

    <div class="volume">176ml</div>

    <div class="dragon-art" role="img" aria-label="Black ink sketch of a chubby, grinning dragon sitting down with small wings and a long tail, breathing a curl of flame"></div>

    <div class="origin-note"><p>MADE USING 100% FRESH<br>AUSTRALIAN PRODUCE</p></div>

    <div class="batch"><p>Batch No<span class="blank"></span></p></div>
  </main>
</body>
</html>
```